Inspirational Quote Poster for Employees

For this project, we need a simple yet high-impact poster template that will be customized for each of our employees with a personalized inspirational quote and color scheme. This template should allow us to quickly and easily customize the text and colors in the poster without a lot of effort.

The poster design should consist of:
- A stylized text area to contain the main text of the quote
- A separate text area to contain the source of quote
- A background that complements the color and style of the text

Text may use different typographic effects (such as color, stroke weight, italicization, font size changes, drop shadows) to draw attention to words in the quote; the source of the quote may be formatted the same as the main text of the quote, or may be formatted differently to distinguish it from the main quote.

The background may be simply a single color, subtle texture, gradients, halftone effects, or other color/texture effects may be used to complement the text.

Examples of the types of posters envisioned by this project:
- http://www.pinvelora.example/marcusdtelford/quillbase-job-1/

Sample quotes to use to build your poster - choose whichever one you want, but be certain that the poster design will handle both long and short quotes:
- "Happiness in intelligent people is the rarest thing I know" - Walden Prosket
- "Wanting to be someone else is a waste of the person you are." - Rolf Dintey
- "Experience is not what happens to you. It is what you do with what happens to you." - Ferris Mundell
- "Simplicity is the ultimate in sophistication." - Rinaldo de Pavesco
- "You will get all you want in life if you help enough other people get what they want." - Tad Pomfrey
- "Hell, there are no rules here — we're trying to accomplish something." - Gareth Vullane

Industry/Entity Type

Quote

Requirements
Must have
• Final deliverable must be:
• - Formatted for an 18” x 24” poster (in portrait orientation)
• - Delivered in Adobe InDesign, Adobe Illustrator, or Extended PostScript format
• - Use CMYK color mode
• - Be print-ready at 300dpi resolution
• - Include any fonts used in the template

```html
<!DOCTYPE html>
<html lang="en">
<head>
<meta charset="utf-8">
<title>Quote Poster – Rolf Dintey</title>
<link rel="stylesheet" href="https://fonts.googleapis.com/css2?family=Oswald:wght@600;700&display=swap">
<style>
  :root {
    --bg-top: #78b9d2;
    --bg-mid: #4fa6c1;
    --bg-bottom: #2a92ab;
    --ink: #1b2c7d;
    --frame: rgba(210, 240, 250, 0.55);
  }
  html, body {
    margin: 0;
    padding: 0;
    width: 848px;
    height: 1200px;
    overflow: hidden;
  }
  .poster {
    position: relative;
    width: 848px;
    height: 1200px;
    background:
      radial-gradient(circle at 20% 30%, rgba(255,255,255,0.06), transparent 40%),
      radial-gradient(circle at 80% 75%, rgba(0,40,60,0.08), transparent 45%),
      linear-gradient(180deg, var(--bg-top) 0%, var(--bg-mid) 55%, var(--bg-bottom) 100%);
    font-family: "Oswald", "Arial Narrow", sans-serif;
    color: var(--ink);
    overflow: hidden;
  }
  .poster__frame {
    position: absolute;
    inset: 27px;
    border: 1px solid var(--frame);
  }
  .quote {
    position: absolute;
    left: 145px;
    top: 160px;
    margin: 0;
    font-weight: 700;
    font-size: 104px;
    line-height: 115px;
    text-transform: uppercase;
    letter-spacing: 0.5px;
  }
  .quote__line {
    display: block;
    white-space: nowrap;
  }
  .quote__line--lead {
    font-size: 92px;
  }
  .quote__initial {
    font-size: 112px;
  }
  .quote__open {
    position: absolute;
    left: -62px;
    top: -4px;
    font-size: 110px;
    line-height: 115px;
  }
  .quote__close {
    display: inline-block;
    margin-left: 10px;
    font-size: 104px;
    line-height: 1;
    vertical-align: top;
    position: relative;
    top: 4px;
  }
  .source {
    position: absolute;
    right: 178px;
    top: 1018px;
    margin: 0;
    font-weight: 700;
    font-size: 50px;
    line-height: 60px;
    text-transform: uppercase;
    letter-spacing: 1px;
    white-space: nowrap;
  }
  .source__small {
    font-size: 40px;
  }
</style>
</head>
<body>
  <main class="poster">
    <div class="poster__frame"></div>

    <blockquote class="quote">
      <span class="quote__open">“</span>
      <span class="quote__line quote__line--lead"><span class="quote__initial">W</span>anting</span>
      <span class="quote__line">to be</span>
      <span class="quote__line">someone</span>
      <span class="quote__line">else is a</span>
      <span class="quote__line">waste of</span>
      <span class="quote__line">the person</span>
      <span class="quote__line">you are.<span class="quote__close">”</span></span>
    </blockquote>

    <p class="source">- R<span class="source__small">olf</span> D<span class="source__small">intey</span></p>
  </main>
</body>
</html>
```